Bright Fern Painting needs a new business card. See attachments for our logo and current card as an example.
We want to utilize the same colors in the logo, and keep all the information that is currently on it. Just need an updated and modern design.
We are open to loosing the Association Logos if it means a better design.
We are also entertaining a spot for a picture of a headshot of the person listed on the card. Head shot can be finished later.

```html
<!DOCTYPE html>
<html lang="en">
<head>
<meta charset="utf-8">
<title>Bright Fern Painting — Business Card</title>
<link rel="stylesheet" href="https://fonts.googleapis.com/css2?family=Mulish:ital,wght@0,700;0,800;1,700&family=Questrial&display=swap">
<style>
  :root {
    --olive: #3e4430;
    --paper: #ffffff;
    --ink: #111111;
    --tick: #1f8a3c;
    --ring: #555555;
    --on-olive: #ffffff;
  }
  * { margin: 0; padding: 0; box-sizing: border-box; }
  html, body {
    width: 1200px; height: 686px; overflow: hidden;
    background: var(--olive);
  }
  .card {
    position: relative; width: 1200px; height: 686px;
    background: var(--olive);
  }
  .card__face {
    position: absolute; left: 13px; top: 15px;
    width: 1171px; height: 518px;
    background: var(--paper);
  }
  .person {
    position: absolute; left: 0; right: 0; top: 74px;
    text-align: center; color: var(--ink);
  }
  .person__name {
    font-family: "Mulish", sans-serif; font-weight: 800;
    font-size: 47px; letter-spacing: 2px; line-height: 1.2;
  }
  .person__title {
    font-family: "Mulish", sans-serif; font-weight: 700; font-style: italic;
    font-size: 35px; line-height: 1.2; margin-top: 2px;
  }
  .services {
    position: absolute; left: 0; right: 0; top: 250px;
    list-style: none; color: var(--ink);
    font-family: "Questrial", sans-serif; font-size: 42px; letter-spacing: 1px;
  }
  .services__item {
    display: flex; justify-content: center; align-items: center;
    height: 52.5px; gap: 20px;
  }
  .services__tick { width: 32px; height: 32px; flex: none; }
  .contact {
    position: absolute; left: 0; right: 0; top: 553px;
    text-align: center; color: var(--on-olive);
  }
  .contact__line {
    font-family: "Questrial", sans-serif; font-size: 42px;
    letter-spacing: 1.5px; line-height: 1.25;
  }
  .contact__web {
    font-family: "Mulish", sans-serif; font-weight: 800;
    font-size: 41px; letter-spacing: 1.5px; line-height: 1.25;
  }
</style>
</head>
<body>
<div class="card">
  <div class="card__face">
    <div class="person">
      <h1 class="person__name">Daniel Harper</h1>
      <p class="person__title">Quality Manager</p>
    </div>
    <ul class="services">
      <li class="services__item">
        <svg class="services__tick" viewBox="0 0 32 32" aria-hidden="true"><circle cx="15" cy="17" r="12" fill="none" stroke="var(--ring)" stroke-width="1.6"/><path d="M9 17 L14 22 L27 6" fill="none" stroke="var(--tick)" stroke-width="2.6" stroke-linecap="round" stroke-linejoin="round"/></svg>
        <span>Exterior Painting</span>
      </li>
      <li class="services__item">
        <svg class="services__tick" viewBox="0 0 32 32" aria-hidden="true"><circle cx="15" cy="17" r="12" fill="none" stroke="var(--ring)" stroke-width="1.6"/><path d="M9 17 L14 22 L27 6" fill="none" stroke="var(--tick)" stroke-width="2.6" stroke-linecap="round" stroke-linejoin="round"/></svg>
        <span>Interior Painting</span>
      </li>
      <li class="services__item">
        <svg class="services__tick" viewBox="0 0 32 32" aria-hidden="true"><circle cx="15" cy="17" r="12" fill="none" stroke="var(--ring)" stroke-width="1.6"/><path d="M9 17 L14 22 L27 6" fill="none" stroke="var(--tick)" stroke-width="2.6" stroke-linecap="round" stroke-linejoin="round"/></svg>
        <span>Carpentry</span>
      </li>
      <li class="services__item">
        <svg class="services__tick" viewBox="0 0 32 32" aria-hidden="true"><circle cx="15" cy="17" r="12" fill="none" stroke="var(--ring)" stroke-width="1.6"/><path d="M9 17 L14 22 L27 6" fill="none" stroke="var(--tick)" stroke-width="2.6" stroke-linecap="round" stroke-linejoin="round"/></svg>
        <span>Drywall</span>
      </li>
    </ul>
  </div>
  <div class="contact">
    <p class="contact__line">262-555-0148 &nbsp;|&nbsp; Daniel.BrightFern@mail.com</p>
    <p class="contact__web">BrightFernPainting.com</p>
  </div>
</div>
</body>
</html>
```